A hand soap seller needs a premium label for a new product

We need a premium label for a bottle of soap. We want to write on it:
VANTROSELLA (Name)
Hypoallergenic and antibacterial hand soap
350 ml e / 11.8 fl oz (volume, http://pimaxo.ru/7K3RtWbqmeL519)
Saint Petersburg - Russia / www.vantrosella.ru
We want to see the face of a hippopotamus in the design. Use only black and white and green for accents (the color of grass). Examples of a hippopotamus are shown in the photo. Our soap is hypoallergenic. Ideal for both children and adults. Therefore, the label should appeal to adults and children.
The bottle will be white, and the soap dispenser will be black.
So I'm attaching an example of a soap design that we liked
Label size: height-78 mm, width-102 mm !!!

Target Market(s)

Mothers and children

Industry/Entity Type

Hand soap

Font styles to use
Serif

Colors

Designer to choose only greyscale colors for use in the design.

Requirements
Must have
• The face of a hippopotamus emerging from the grass, Black and white palette with elements of green (grass color)
Nice to have
• The face of a hippopotamus emerging from the grass
Should not have
• Different colors

```html
<!DOCTYPE html>
<html lang="en">
<head>
<meta charset="utf-8">
<title>Vantrosella Hand Soap Labels</title>
<link href="https://fonts.googleapis.com/css2?family=Anton&family=Oswald:wght@600&family=Open+Sans:wght@700&display=swap" rel="stylesheet">
<style>
  :root {
    --ink: #1b1b1b;
    --paper: #ffffff;
    --stage: #ececec;
    --grass: #4caf3a;
    --art-light: #e4e4e4;
    --art-mid: #bdbdbd;
  }
  html, body {
    margin: 0;
    padding: 0;
    width: 1156px;
    height: 1200px;
    overflow: hidden;
    background: var(--stage);
  }
  .stage {
    width: 1156px;
    height: 1200px;
    display: flex;
    flex-direction: column;
    justify-content: center;
    align-items: center;
    gap: 40px;
  }
  .label {
    width: 700px;
    height: 535px;
    background: var(--paper);
    box-shadow: 0 2px 10px rgba(0,0,0,0.08);
    overflow: hidden;
  }
  .label svg { display: block; }
  .brand-title {
    font-family: "Anton", "Oswald", sans-serif;
    fill: var(--ink);
  }
  .info-line {
    font-family: "Oswald", sans-serif;
    font-weight: 600;
    fill: var(--paper);
  }
  .arc-line {
    font-family: "Oswald", sans-serif;
    font-weight: 600;
    fill: var(--ink);
  }
  .accent-line {
    font-family: "Oswald", sans-serif;
    font-weight: 600;
    fill: var(--grass);
  }
  .site-line {
    font-family: "Open Sans", sans-serif;
    font-weight: 700;
    fill: var(--paper);
  }
</style>
</head>
<body>
<main class="stage">

  <section class="label label--wave">
    <svg width="700" height="535" viewBox="0 0 700 535">
      <defs>
        <linearGradient id="hippoHeadTone" x1="0" y1="0" x2="0" y2="1">
          <stop offset="0" stop-color="var(--art-light)"/>
          <stop offset="1" stop-color="var(--art-mid)"/>
        </linearGradient>
      </defs>
      <text class="brand-title" x="350" y="130" text-anchor="middle" font-size="108" textLength="600" lengthAdjust="spacingAndGlyphs">VANTROSELLA</text>
      <rect class="hippo-art" x="255" y="150" width="190" height="170" rx="50" fill="url(#hippoHeadTone)" role="img" aria-label="Illustration of a hippopotamus face rising out of the grass"/>
      <path class="grass-edge" d="M0 322 C 150 272, 330 262, 460 297 C 560 324, 640 302, 700 282" fill="none" stroke="var(--grass)" stroke-width="10"/>
      <path class="wave-band" d="M0 330 C 150 280, 330 270, 460 305 C 560 332, 640 310, 700 290 L700 535 L0 535 Z" fill="var(--ink)"/>
      <text class="info-line" x="350" y="388" text-anchor="middle" font-size="25" textLength="620" lengthAdjust="spacingAndGlyphs">HYPOALLERGENIC &amp; ANTIBACTERIAL HAND SOAP</text>
      <text class="info-line" x="350" y="432" text-anchor="middle" font-size="26">350 ML E / 11,8 FL.OZ.</text>
      <text class="info-line" x="350" y="468" text-anchor="middle" font-size="22">SAINTS-PETERSBURG – RUSSIA</text>
      <text class="site-line" x="350" y="505" text-anchor="middle" font-size="18">www.vantrosella.ru</text>
    </svg>
  </section>

  <section class="label label--badge">
    <svg width="700" height="535" viewBox="0 0 700 535">
      <defs>
        <path id="badgeArc" d="M240 222 A 110 110 0 0 0 460 222"/>
      </defs>
      <text class="brand-title" x="350" y="112" text-anchor="middle" font-size="96" textLength="560" lengthAdjust="spacingAndGlyphs">VANTROSELLA</text>
      <circle class="badge-disc" cx="350" cy="222" r="86" fill="var(--ink)" stroke="var(--grass)" stroke-width="5"/>
      <rect class="hippo-art" x="292" y="180" width="116" height="84" rx="28" fill="var(--art-light)" role="img" aria-label="Illustration of a standing baby hippopotamus inside the black circle"/>
      <text class="arc-line" font-size="22" letter-spacing="1">
        <textPath href="#badgeArc" startOffset="50%" text-anchor="middle">HYPOALLERGENIC HAND SOAP</textPath>
      </text>
      <text class="accent-line" x="350" y="378" text-anchor="middle" font-size="18" letter-spacing="4">ANTIBACTERIAL</text>
      <rect class="base-band" x="0" y="395" width="700" height="140" fill="var(--ink)"/>
      <rect class="grass-strip" x="0" y="395" width="700" height="6" fill="var(--grass)"/>
      <text class="info-line" x="350" y="438" text-anchor="middle" font-size="26">350 ML E / 11,8 FL.OZ.</text>
      <text class="info-line" x="350" y="474" text-anchor="middle" font-size="22">SAINTS-PETERSBURG – RUSSIA</text>
      <text class="site-line" x="350" y="509" text-anchor="middle" font-size="18">www.vantrosella.ru</text>
    </svg>
  </section>

</main>
</body>
</html>
```